Classic/Royal 5 Items Black coloured Stationery Design

Hello,
I'm looking for an Elegant Stationery set consists of 5 items as the following,
1- Letterhead
2- Business Card
3- Invoice
4- CD/DVD with their Envelope Design
5- Envelope
To let the project move ahead easily, I've included a folder consists many designs I liked from various design sites and it consists of,
1- Business card
2- Corporate Identity
3- Invoice
4- Miscellanies
Inside the first three folders, you will find a folder named "Recommended", it contains designs that I like so much and hoping to have a design like them.
The "Miscellanies" folder got some designs for Inspiration.
I'm waiting for some greats designs, a joomla template designer is a bonus for me as I will need him to design the website layer soon.
Due to upload problems at ArtHarbor, I've uploaded the folder in a .rar archive at multiple site and here is the link http://filevanta.example/QZTRLPNB .
Thank you
Update :- You can use this alternative download link from my Nimbox drive to download the designs
https://share.cloudvessel.example/file/d/7Hq2pLx9w4t6KmZr83VnbYsQ5eJd
Business

```html
<!DOCTYPE html>
<html lang="en">
<head>
<meta charset="utf-8">
<title>Velmora Stationery Set</title>
<link rel="stylesheet" href="https://fonts.googleapis.com/css2?family=Playfair+Display:wght@400;600&family=Lato:wght@400;700&display=swap">
<style>
:root{
  --bg:#2a1a0c;
  --bg-edge:#140c05;
  --ink:#1c1a18;
  --panel:#26221f;
  --panel-dark:#181614;
  --gold:#d4a640;
  --gold-light:#f3d27a;
  --gold-deep:#8a6418;
  --paper:#ffffff;
  --text:#3a3632;
  --muted:#8b857e;
}
*{box-sizing:border-box;margin:0;padding:0}
html,body{width:1200px;height:848px;overflow:hidden}
body{background:radial-gradient(ellipse at 50% 45%,var(--bg) 0%,var(--bg-edge) 100%);font-family:"Lato",sans-serif;position:relative}
.piece{position:absolute;box-shadow:0 10px 30px rgba(0,0,0,.55)}
.gold-band{background:linear-gradient(180deg,var(--gold-deep),var(--gold-light) 45%,var(--gold) 60%,var(--gold-deep))}
.brand{font-family:"Playfair Display",serif;font-weight:400;color:var(--gold);display:flex;align-items:center;gap:8px;white-space:nowrap}
.brand-mark{border:1.5px solid currentColor;display:inline-block}
.brand--ink{color:var(--ink)}
.tagline{font-size:8px;letter-spacing:.5px;color:var(--gold);font-family:"Lato",sans-serif}

/* folder */
.folder{left:60px;top:150px;width:300px;height:590px;background:linear-gradient(160deg,var(--panel) 0%,var(--panel-dark) 100%);display:flex;flex-direction:column;align-items:center;justify-content:center}
.folder .brand{font-size:34px}
.folder .brand-mark{width:34px;height:34px}
.folder__footer{position:absolute;left:0;right:0;bottom:0;height:34px;display:flex;align-items:flex-start}
.folder__footer .gold-band{height:6px;width:100%}
.folder__tag{position:absolute;bottom:14px;width:100%;text-align:center}

/* letterhead */
.letterhead{left:400px;top:40px;width:380px;height:538px;background:var(--paper);padding:36px 34px 0;color:var(--text)}
.letterhead .brand{justify-content:center;font-size:24px}
.letterhead .brand-mark{width:22px;height:22px}
.letter{margin-top:46px;font-size:6.4px;line-height:1.55}
.letter h2{font-family:"Lato",sans-serif;font-weight:400;font-size:12px;color:var(--ink);margin-bottom:8px}
.letter p{margin-bottom:10px;text-align:justify}
.signature{width:54px;height:16px;background:linear-gradient(90deg,#d8d4cf,#eeeae6);margin:6px 0 4px}
.letterhead__footer{position:absolute;left:0;right:0;bottom:0;height:38px;background:var(--panel);display:flex;gap:18px;padding:10px 34px 0;font-size:6px;color:#cfc8bd;line-height:1.5}
.letterhead__footer .gold-band{position:absolute;left:0;right:0;top:0;height:4px}
.letterhead__footer .col{border-left:1px solid var(--gold-deep);padding-left:6px}
.letterhead__footer .label{color:var(--gold)}

/* business cards */
.card{width:220px;height:126px;background:linear-gradient(160deg,var(--panel),var(--panel-dark))}
.card .gold-band{position:absolute;left:0;right:0;height:3px}
.card--front{left:820px;top:40px;display:flex;align-items:center;justify-content:center}
.card--front .brand{font-size:17px}
.card--front .brand-mark{width:14px;height:14px}
.card--back{left:820px;top:184px;padding:26px 18px;color:#cfc8bd;font-size:6.5px;line-height:1.6}
.card--back .name{color:var(--gold);font-size:9px;letter-spacing:.5px;text-align:right}
.card--back .role{text-align:right;margin-bottom:28px}
.card--back .contact{display:flex;justify-content:space-between}

/* cd */
.cd{left:820px;top:340px;width:220px;height:220px}
.cd-label{position:absolute;left:0;top:0;width:220px;height:220px;display:flex;flex-direction:column;align-items:center;justify-content:flex-end;padding-bottom:40px;pointer-events:none}
.cd-label .brand{font-size:16px}
.cd-label .brand-mark{width:12px;height:12px}

/* envelope */
.envelope{left:400px;top:608px;width:380px;height:200px;background:var(--paper);overflow:hidden}
.envelope__flap{position:absolute;left:0;right:0;top:0;height:60px;background:var(--panel)}
.envelope__flap .gold-band{position:absolute;left:0;right:0;bottom:0;height:3px}
.envelope__flap .brand{position:absolute;left:0;right:0;top:14px;justify-content:center;font-size:16px}
.envelope__flap .brand-mark{width:12px;height:12px}
.envelope__edge{position:absolute;left:0;top:0;bottom:0;width:6px}

/* cd sleeve */
.sleeve{left:820px;top:588px;width:220px;height:220px;background:linear-gradient(160deg,#3a3330,#1e1b19);display:flex;flex-direction:column;align-items:center;justify-content:center;gap:6px}
.sleeve .brand{font-size:20px}
.sleeve .brand-mark{width:16px;height:16px}
</style>
</head>
<body>

<section class="piece folder" aria-label="Presentation folder">
  <div class="brand"><span class="brand-mark"></span>Velmora</div>
  <div class="folder__footer"><div class="gold-band"></div></div>
  <div class="folder__tag tagline">Hotels and General Supplies</div>
</section>

<section class="piece letterhead" aria-label="Letterhead">
  <div class="brand brand--ink"><span class="brand-mark"></span>Velmora</div>
  <div class="letter">
    <h2>Dear Alex Marlow</h2>
    <p>Lorem ipsum dolor sit amet, consectetur adipiscing elit. Sed ut ante mauris eleifend, quam a vulputate dictum, massa quam dapibus leo, eget vulputate orci purus ut lorem. In fringilla nisi in ligula pellentesque aliquam.</p>
    <p>Nulla facilisi. Nunc volutpat vestibulum ante ipsum primis in faucibus orci luctus et ultrices posuere cubilia curae. Ut sit amet orci vel mauris blandit vehicula.</p>
    <p>Sed eget turpis a pede tempor malesuada. Vivamus quis mi at leo pulvinar hendrerit. Cum sociis natoque penatibus et magnis dis parturient montes.</p>
    <p style="margin-bottom:0">Sincerely,</p>
    <div class="signature" role="img" aria-label="Handwritten signature"></div>
    <p>Alex Marlow</p>
  </div>
  <footer class="letterhead__footer">
    <div class="gold-band"></div>
    <div class="col">Velmora<br>Hotels and General Supplies</div>
    <div class="col">Lane 45<br>Town, Region, 4020</div>
    <div class="col"><span class="label">phone</span> 0198765432<br><span class="label">email</span> info@velmora.example</div>
  </footer>
</section>

<section class="piece card card--front" aria-label="Business card front">
  <div class="gold-band" style="top:0"></div>
  <div class="brand"><span class="brand-mark"></span>Velmora</div>
</section>

<section class="piece card card--back" aria-label="Business card back">
  <div class="gold-band" style="top:0"></div>
  <div class="name">ALEX MARLOW</div>
  <div class="role">Sales Manager</div>
  <div class="contact"><span>Lane 45, Town, Region, 4020</span><span>0198765432</span><span>info@velmora.example</span></div>
</section>

<section class="piece cd" aria-label="CD label" style="box-shadow:none">
  <svg width="220" height="220" viewBox="0 0 220 220">
    <defs>
      <radialGradient id="cdBody" cx="50%" cy="40%" r="60%">
        <stop offset="0" stop-color="#2c2724"/><stop offset="1" stop-color="#141210"/>
      </radialGradient>
    </defs>
    <circle cx="110" cy="110" r="108" fill="url(#cdBody)" stroke="#c9c9c9" stroke-width="3"/>
    <circle cx="110" cy="110" r="30" fill="#d9d9d9"/>
    <circle cx="110" cy="110" r="22" fill="#8a8a8a"/>
    <circle cx="110" cy="110" r="15" fill="#6b4a1f"/>
  </svg>
  <div class="cd-label">
    <div class="brand"><span class="brand-mark"></span>Velmora</div>
    <div class="tagline">Hotels and General Supplies</div>
  </div>
</section>

<section class="piece envelope" aria-label="Envelope">
  <div class="envelope__flap">
    <div class="brand"><span class="brand-mark"></span>Velmora</div>
    <div class="gold-band"></div>
  </div>
  <div class="envelope__edge gold-band"></div>
</section>

<section class="piece sleeve" aria-label="CD sleeve">
  <div class="brand"><span class="brand-mark"></span>Velmora</div>
  <div class="tagline">Hotels and General Supplies</div>
</section>

</body>
</html>
```